Floor Inspections and Consulting

We provide inspections and consulting services on various floor coverings, e.g. carpet, hardwood, etc. We also do expert witness work for attorneys due to floor covering failures. We current have a logo, just need it incorporated into a new design. I have examples of cards I have found on the internet that capture my attention and make a statement. I have included our original business card, which in my opinion is terrible, but it does have our logo on it.

```html
<!DOCTYPE html>
<html lang="en">
<head>
<meta charset="utf-8">
<title>Summit Floor Inspections – Business Card</title>
<link href="https://fonts.googleapis.com/css2?family=Montserrat:wght@500;700;800&family=Roboto:wght@400;700&display=swap" rel="stylesheet">
<style>
  :root {
    --backdrop: #3a3430;
    --card: #111111;
    --accent: #f5a000;
    --steel: #c9c9c9;
    --grey-text: #bdbdbd;
    --white: #f2f2f2;
    --divider: #2c2c2c;
  }
  * { box-sizing: border-box; margin: 0; padding: 0; }
  html, body {
    width: 1200px; height: 844px; overflow: hidden;
    background: var(--backdrop);
  }
  .canvas {
    width: 1200px; height: 844px;
    display: flex; align-items: center; justify-content: center; gap: 48px;
  }
  .card {
    width: 532px; height: 304px;
    background: var(--card);
    border-radius: 3px;
    box-shadow: 0 10px 28px rgba(0,0,0,.45);
    position: relative;
  }

  /* Contact side */
  .card--contact { display: flex; }
  .brand-block {
    width: 50%;
    display: flex; align-items: center; justify-content: center;
    padding-left: 10px;
  }
  .brand-name {
    font-family: "Montserrat", sans-serif; font-weight: 800;
    color: var(--accent); font-size: 22px; line-height: 1.1;
    text-transform: uppercase; text-align: center; letter-spacing: .5px;
  }
  .divider {
    width: 1px; background: var(--divider);
    margin: 70px 0;
  }
  .contact-block {
    flex: 1; padding: 82px 0 0 26px;
    font-family: "Roboto", sans-serif;
  }
  .person-name {
    font-family: "Montserrat", sans-serif; font-weight: 800;
    color: var(--accent); font-size: 17px; letter-spacing: .5px;
    text-transform: uppercase; margin-bottom: 18px;
  }
  .contact-list { list-style: none; }
  .contact-item {
    display: flex; align-items: center; gap: 8px;
    color: var(--grey-text); font-size: 14px; margin-bottom: 8px;
  }
  .contact-icon { width: 14px; height: 14px; flex: none; }

  /* Brand side */
  .card--brand {
    display: flex; flex-direction: column; align-items: center; justify-content: center;
    text-align: center;
  }
  .brand-name--steel {
    color: var(--steel); font-size: 28px;
  }
  .tagline {
    display: flex; align-items: center; gap: 8px;
    font-family: "Montserrat", sans-serif; font-weight: 500;
    color: var(--steel); font-size: 10px; letter-spacing: 2px;
    margin-top: 8px; text-transform: uppercase;
  }
  .tagline::before, .tagline::after {
    content: ""; width: 36px; height: 1px; background: var(--steel);
  }
  .statement {
    font-family: "Roboto", sans-serif; font-weight: 700;
    color: var(--white); font-size: 15px; margin-top: 34px;
  }
</style>
</head>
<body>
<main class="canvas">
  <section class="card card--contact">
    <div class="brand-block">
      <p class="brand-name">Summit Floor<br>Inspections</p>
    </div>
    <div class="divider"></div>
    <div class="contact-block">
      <h1 class="person-name">Daniel Harrow</h1>
      <ul class="contact-list">
        <li class="contact-item">
          <svg class="contact-icon" viewBox="0 0 14 14" aria-hidden="true">
            <rect x="0.5" y="0.5" width="13" height="13" rx="2" fill="none" stroke="var(--accent)"/>
            <path d="M4 3.5 L5.5 3.5 L6 5.5 L5 6.3 Q6 8.3 7.7 9 L8.5 8 L10.5 8.5 L10.5 10 Q6 10.5 3.8 5 Z" fill="var(--accent)"/>
          </svg>
          303-555-0142
        </li>
        <li class="contact-item">
          <svg class="contact-icon" viewBox="0 0 14 14" aria-hidden="true">
            <rect x="0.5" y="2.5" width="13" height="9" rx="1" fill="var(--accent)"/>
            <path d="M1 3 L7 8 L13 3" fill="none" stroke="var(--card)" stroke-width="1.2"/>
          </svg>
          daniel@summitfloorpro.com
        </li>
        <li class="contact-item">
          <svg class="contact-icon" viewBox="0 0 14 14" aria-hidden="true">
            <circle cx="7" cy="7" r="6.5" fill="var(--accent)"/>
            <path d="M0.8 7 H13.2 M7 0.8 V13.2 M2 3.8 H12 M2 10.2 H12" stroke="var(--card)" stroke-width="0.8"/>
            <ellipse cx="7" cy="7" rx="3" ry="6.3" fill="none" stroke="var(--card)" stroke-width="0.8"/>
          </svg>
          www.summitfloorpro.com
        </li>
      </ul>
    </div>
  </section>

  <section class="card card--brand">
    <p class="brand-name brand-name--steel">Summit Floor<br>Inspections</p>
    <p class="tagline">Analysis &amp; Consulting</p>
    <p class="statement">Certified Floor Covering Inspection &amp; Consulting</p>
  </section>
</main>
</body>
</html>
```